Visitenkarten für Mentorin für Frauen
Zielgruppe
Ich bin Mentorin für Frauen (30-50 Jahre alt), die ihre Berufung endlich finden möchten und sich nach mehr Energie und Sinn sehnen. Ich helfe ihnen mit meiner (Name fehtl noch)-Methode ihren Seelenweg zu finden und zu gehen, sodass sie vor Energie übersprudeln und mit einem Leuchten in den Augen ein Leben in Fluss und Fülle kreieren.
Sie sind nicht unglücklich, aber es fehtl ihnen was, das sie wirklich erfüllt.
Stichwörter: Numerologie, Human Design, Seelenweg, Berufung, Lebensaufgabe, erfüllt sein- endlich die Leere füllen, Freiheit, Selbstbestimmt, Selbstliebe, Potentialentfaltung, Transformation
meine core story:
Mit Freude, unglaublicher Energie und einem Strahlen in den Augen schon vor dem Wecker aufzustehen, war für mich früher undenkbar. Ich konnte mir nicht vorstellen, wie sich Leute auf den Montag freuen konnten.
Dabei hätte mich nicht als unglücklich bezeichnet, aber es fehlt einfach etwas, ich hatte eine innere Leere und eine Sehnsucht nach dem Sinn in meinem Lebe, wollte so geliebt werden wie ich bin und mich auch so zeigen können. Ich weiß wie es ist sich klein, unsicher zu fühlen und nicht zu wissen woher das kommt. Ich habe es einfach nicht für möglich gehalten, dass diese innere Leere so leicht zu füllen ist und Freude, Spaß, Selbstbewusstseein und Leichtigkeit in allen Bereichen mit sich bringt.
Weil ich selbst diesen Weg gegangen bin und weil ich weiß, dass es nichts erfüllenderes gibt als das schlummernde Potential zu erwecken, begleite ich Frauen dabei ihren Seelenweg zu finden und zu gehen.
Dadurch dass sie genau wissen, was ihre Gaben sind und was ihre Seele glücklich macht, haben sie Spaß und Freude, gerade auch in den alltäglichen Dingen. Sie führen ein selbstbestimmtes Leben, lieben sich selbst und zeigen sich so wie sie sind.Die gigantische Energie die dadurch in ihnen frei wird, lässt sie die bisherigen Grenzen überwinden. Sie tun was sie erfüllt, o..
Aufgabenstellung
weiblich, geschwungen, weich: beinhalten solls:
Hannelore Wiebke
Mentorin für Powerfrauen
(Lebe deine Berufung)--> da bin ich mir nicht ganz sicher ob das gut aussehn wird oder zuviel wird
falls relevant habe ich bisher folgende Schriftarten verwendet: Canva Sans und Tan mon cheri
ist aber kein muss

```html
<!DOCTYPE html>
<html lang="de">
<head>
<meta charset="utf-8">
<title>Hannelore Wiebke – Visitenkarte</title>
<link rel="stylesheet" href="https://fonts.googleapis.com/css2?family=Sacramento&family=Cormorant+Garamond:wght@500&display=swap">
<style>
  :root {
    --card-bg: #f4e4dc;
    --card-bg-light: #f7ebe5;
    --name-colour: #c03a72;
    --tagline-colour: #4f4a49;
    --floral-tone: #d49084;
    --floral-tone-soft: rgba(212, 144, 132, 0);
  }
  html, body {
    margin: 0;
    padding: 0;
    width: 1200px;
    height: 686px;
    overflow: hidden;
  }
  .business-card {
    position: relative;
    width: 1200px;
    height: 686px;
    background: radial-gradient(ellipse at 50% 50%, var(--card-bg-light) 0%, var(--card-bg) 75%);
    overflow: hidden;
  }
  .floral-corner {
    position: absolute;
  }
  .floral-corner--top-right {
    right: 0;
    top: 0;
    width: 230px;
    height: 280px;
    background: radial-gradient(ellipse at 80% 25%, rgba(212, 144, 132, 0.45) 0%, var(--floral-tone-soft) 70%);
  }
  .floral-corner--bottom-left {
    left: 0;
    bottom: 0;
    width: 230px;
    height: 250px;
    background: radial-gradient(ellipse at 25% 80%, rgba(212, 144, 132, 0.45) 0%, var(--floral-tone-soft) 70%);
  }
  .card-name {
    position: absolute;
    left: 0;
    right: 0;
    top: 200px;
    margin: 0;
    text-align: center;
    font-family: "Sacramento", cursive;
    font-weight: 400;
    font-size: 158px;
    line-height: 1;
    color: var(--name-colour);
    letter-spacing: 0.02em;
  }
  .card-tagline {
    position: absolute;
    left: 0;
    right: 0;
    top: 408px;
    margin: 0;
    text-align: center;
    font-family: "Cormorant Garamond", serif;
    font-weight: 500;
    font-size: 42px;
    line-height: 1;
    letter-spacing: 0.24em;
    text-transform: uppercase;
    color: var(--tagline-colour);
    padding-left: 0.24em;
  }
</style>
</head>
<body>
  <main class="business-card">
    <div class="floral-corner floral-corner--top-right" role="img" aria-label="Zarte Blütenzweige in Roségold, von oben rechts herabhängend"></div>
    <div class="floral-corner floral-corner--bottom-left" role="img" aria-label="Zarte Blütenzweige in Roségold, von unten links aufsteigend"></div>
    <h1 class="card-name">Hannelore Wiebke</h1>
    <p class="card-tagline">Lebe deine Berufung</p>
  </main>
</body>
</html>
```